Email Signature Gif Animation Design

We are looking for an interactive Email Signature to Standardize around for our growing company.

We are a commerical electrical contractor based out of North Jersey. We have a big corporate client tele and perfer a more professional fresh looking signature with titles and perhaps a suttle animation for effect.

Attached below is our company logo which is to be used prominently in the emai signature. We would consider a "refresh' of our logo design provided it does deviate too much.

We would like the tag Line "The Norvale Electric Path" worked into that signature as a option.
Updates

Reviewing designs and am underwhelmed with the creativiity and designs, this is anyones prize!

Target Market(s)

Corporate / Middle Managers

Industry/Entity Type

Electrical Contracting & Engineering

Colors
FFF300
FFF600
FEFA6F
FFFEC7
FFFEE8

Requirements
Must have
• Must have, First & Last Name of Employee, Title of Employee, Office & Cell Phone Number, Email Address
Nice to have
• Gif Animation

```html
<!DOCTYPE html>
<html lang="en">
<head>
<meta charset="UTF-8">
<title>Norvale Electric – Email Signature</title>
<link rel="stylesheet" href="https://fonts.googleapis.com/css2?family=Montserrat:wght@600;700&display=swap">
<style>
  :root {
    --canvas-bg: #ffffff;
    --brand-mark: #e3e3e3;
    --detail-faded: #ececec;
    --divider: #e6e6e6;
    --band-dark: #1f1f1f;
    --band-gold: #c9a227;
  }
  * { margin: 0; padding: 0; box-sizing: border-box; }
  html, body {
    width: 1200px;
    height: 192px;
    overflow: hidden;
    background: var(--canvas-bg);
  }
  .signature {
    position: relative;
    width: 1200px;
    height: 192px;
    background: var(--canvas-bg);
  }
  .brand-name {
    position: absolute;
    left: 29px;
    top: 48px;
    width: 190px;
    font-family: "Montserrat", sans-serif;
    font-weight: 700;
    font-size: 31px;
    line-height: 40px;
    color: var(--brand-mark);
    white-space: nowrap;
  }
  .divider {
    position: absolute;
    left: 233px;
    top: 38px;
    width: 3px;
    height: 100px;
    background: var(--divider);
  }
  .contact {
    position: absolute;
    left: 262px;
    top: 44px;
    font-family: "Montserrat", sans-serif;
    font-weight: 600;
    color: var(--detail-faded);
    white-space: nowrap;
  }
  .contact__name { font-size: 20px; line-height: 26px; font-weight: 700; }
  .contact__title { font-size: 14px; line-height: 22px; }
  .contact__line { font-size: 13px; line-height: 20px; }
  .footer-band {
    position: absolute;
    left: 0;
    bottom: 0;
    width: 1200px;
    height: 19px;
    display: flex;
  }
  .footer-band__dark { width: 779px; background: var(--band-dark); }
  .footer-band__gold { flex: 1; background: var(--band-gold); }
</style>
</head>
<body>
  <div class="signature">
    <div class="brand-name">Norvale<br>Electric</div>
    <div class="divider"></div>
    <div class="contact">
      <p class="contact__name">Jordan Hale</p>
      <p class="contact__title">Project Manager</p>
      <p class="contact__line">Office 555-014-2200 &nbsp;·&nbsp; Cell 555-014-3311</p>
      <p class="contact__line">jhale@norvaleelectric.com</p>
    </div>
    <div class="footer-band">
      <div class="footer-band__dark"></div>
      <div class="footer-band__gold"></div>
    </div>
  </div>
</body>
</html>
```